Tooth whitening strip packaging

We have some 4 oral care products that want to completely rebrand and change their packaging

Target Market(s)

Everyone

Industry/Entity Type

Oral care

Other font styles liked:
• We like simple and elegant font

Requirements
Must have
• 1) elegant, high tech, cutting-edge technology look 2) all the products should have the same branding scheme 3) we want the amazing look of these packages increase our sales

```html
<!DOCTYPE html>
<html lang="en">
<head>
<meta charset="utf-8">
<title>Lumqa Whitening Pen – Packaging</title>
<link href="https://fonts.googleapis.com/css2?family=Outfit:wght@400;500;600;700&display=swap" rel="stylesheet">
<style>
  :root {
    --purple: #3a2162;
    --ink: #2e1a5b;
    --pink: #d81b7c;
    --pink-soft: #ec6fb8;
    --white: #ffffff;
    --tick: #2fae4a;
    --scene-top: #c4c4c4;
    --scene-bottom: #e9e9e9;
    --dieline-bg: #787878;
  }
  * { box-sizing: border-box; margin: 0; padding: 0; }
  html, body { width: 1200px; height: 2186px; overflow: hidden; }
  body { position: relative; font-family: "Outfit", sans-serif; color: var(--white); background: var(--dieline-bg); }

  .showcase { position: absolute; left: 0; top: 0; width: 1200px; height: 986px;
    background: linear-gradient(180deg, var(--scene-top), var(--scene-bottom)); }
  .dieline { position: absolute; left: 0; top: 986px; width: 1200px; height: 1200px; background: var(--dieline-bg); }

  /* ---------- front panel (reusable) ---------- */
  .front-panel { position: absolute; width: 291px; height: 653px; background: var(--purple); overflow: hidden; }
  .showcase .front-panel { left: 404px; top: 52px; transform: scale(1.35); transform-origin: 0 0;
    box-shadow: 0 10px 30px rgba(0,0,0,.18); }
  .dieline .front-panel { left: 280px; top: 271px; }
  .fp-logo { position: absolute; left: 0; right: 0; top: 38px; text-align: center; font-size: 50px; font-weight: 700; letter-spacing: -1px; }
  .fp-title { position: absolute; left: 34px; top: 150px; font-size: 40px; font-weight: 500; line-height: 42px; letter-spacing: .5px; }
  .fp-sub { position: absolute; left: 34px; top: 236px; font-size: 19px; color: var(--pink-soft); }
  .fp-nine { position: absolute; left: 24px; top: 292px; width: 66px; height: 72px; }
  .fp-nine-text { position: absolute; left: 90px; top: 305px; font-size: 12.5px; font-weight: 700; line-height: 13px; }
  .fp-seal { position: absolute; left: 184px; top: 298px; width: 62px; height: 62px; }
  .fp-band { position: absolute; left: 0; right: 0; top: 406px; height: 54px; background: var(--pink); }
  .fp-flavor { position: absolute; left: 34px; top: 418px; font-size: 21px; font-weight: 600; }
  .fp-mint { position: absolute; left: 178px; top: 376px; width: 78px; height: 64px; border-radius: 50%;
    background: radial-gradient(circle at 45% 45%, #6fd14a, #2f9a2a 60%, #1f6e1e); }
  .fp-white { position: absolute; left: 0; right: 0; top: 460px; bottom: 0; background: var(--white); }
  .fp-benefits { position: absolute; left: 34px; top: 478px; list-style: none; color: var(--ink); font-size: 17px; line-height: 26px; }
  .fp-benefits li { display: flex; align-items: center; gap: 4px; }
  .fp-benefits li::before { content: ""; width: 8px; height: 8px; border-radius: 50%; background: var(--tick); }
  .fp-rule { position: absolute; left: 34px; right: 0; top: 573px; height: 1px; background: var(--pink); }
  .fp-qty { position: absolute; left: 34px; top: 588px; font-size: 27px; font-weight: 600; color: var(--ink); }

  /* ---------- dieline parts ---------- */
  .dieline-shapes { position: absolute; left: 0; top: 0; }
  .tuck-logo { position: absolute; width: 291px; top: 218px; text-align: center; font-size: 28px; font-weight: 700; letter-spacing: -.5px; }

  .side-panel { position: absolute; top: 271px; width: 75px; height: 653px; background: var(--purple); }
  .side-panel.left { left: 205px; }
  .side-panel.right { left: 571px; }
  .side-band { position: absolute; left: 0; right: 0; top: 406px; height: 54px; background: var(--pink); }
  .side-white { position: absolute; left: 0; right: 0; top: 460px; bottom: 0; background: var(--white); }
  .side-feature { position: absolute; left: 0; right: 0; text-align: center; font-size: 10px; line-height: 11px; }
  .side-feature svg { display: block; margin: 0 auto 3px; }
  .side-vertical { position: absolute; left: 50%; top: 556px; transform: translate(-50%, -50%) rotate(-90deg);
    color: var(--ink); font-size: 21px; font-weight: 700; line-height: 22px; white-space: nowrap; }
  .side-logo { position: absolute; left: 50%; top: 556px; transform: translate(-50%, -50%) rotate(90deg);
    color: var(--purple); font-size: 36px; font-weight: 700; white-space: nowrap; }

  .back-panel { position: absolute; left: 646px; top: 271px; width: 291px; height: 653px; background: var(--purple); }
  .back-header { position: absolute; left: 0; right: 0; top: 0; height: 63px; background: var(--pink);
    display: flex; align-items: center; gap: 18px; padding-left: 26px; }
  .back-brand { font-size: 36px; font-weight: 700; letter-spacing: -.5px; }
  .back-product { font-size: 16px; font-weight: 500; line-height: 17px; }
  .back-copy { position: absolute; left: 25px; top: 83px; width: 240px; font-size: 9.4px; line-height: 13px; }
  .back-copy h3 { color: var(--pink-soft); font-size: 11.5px; font-weight: 600; margin-bottom: 2px; }
  .back-copy section { margin-bottom: 14px; }
  .back-copy ul { list-style: none; }
  .back-copy li { position: relative; padding-left: 10px; margin-bottom: 5px; }
  .back-copy li::before { content: "•"; position: absolute; left: 0; }
  .back-storage { display: flex; justify-content: space-between; }
  .back-rule { position: absolute; left: 18px; right: 18px; top: 570px; height: 1px; background: var(--pink-soft); }
  .back-marks { position: absolute; left: 0; right: 0; top: 582px; display: flex; justify-content: center; gap: 10px; }
  .back-facility { position: absolute; left: 0; right: 0; top: 608px; text-align: center; font-size: 7.5px; }
  .glue-flap { position: absolute; left: 937px; top: 271px; width: 61px; height: 653px; background: var(--purple); }
</style>
</head>
<body>

<!-- ===== Flat front face ===== -->
<div class="showcase">
  <div class="front-panel">
    <div class="fp-logo">lumqa.</div>
    <div class="fp-title">WHITENING<br>PEN</div>
    <div class="fp-sub">Professional Results</div>
    <svg class="fp-nine" viewBox="0 0 66 72" aria-hidden="true">
      <circle cx="33" cy="36" r="30" fill="none" stroke="var(--pink-soft)" stroke-width="5" stroke-dasharray="1.6 3.2"/>
      <text x="27" y="58" text-anchor="middle" font-family="Outfit, sans-serif" font-weight="700" font-size="60" fill="#fff">9</text>
    </svg>
    <div class="fp-nine-text">UP TO<br>TIMES<br>WHITER</div>
    <svg class="fp-seal" viewBox="0 0 62 62" role="img" aria-label="Approval seal">
      <circle cx="31" cy="31" r="29" fill="none" stroke="#fff" stroke-width="2"/>
      <circle cx="31" cy="31" r="17" fill="none" stroke="#fff" stroke-width="1.5"/>
    </svg>
    <div class="fp-band"></div>
    <div class="fp-flavor">Mint Flavor</div>
    <div class="fp-mint" role="img" aria-label="Fresh mint leaves"></div>
    <div class="fp-white"></div>
    <ul class="fp-benefits">
      <li>Safe on Enamel</li>
      <li>Instant Effect</li>
      <li>Whiten Years of Stains</li>
    </ul>
    <div class="fp-rule"></div>
    <div class="fp-qty">4 x 2ml</div>
  </div>
</div>

<!-- ===== Carton dieline ===== -->
<div class="dieline">
  <svg class="dieline-shapes" width="1200" height="1200" viewBox="0 0 1200 1200" aria-hidden="true">
    <path d="M280 271 V165 Q280 135 310 135 H541 Q571 135 571 165 V271 Z" fill="var(--purple)"/>
    <path d="M646 271 V165 Q646 135 676 135 H907 Q937 135 937 165 V271 Z" fill="var(--purple)"/>
    <path d="M646 924 H937 V1030 Q937 1060 907 1060 H676 Q646 1060 646 1030 Z" fill="var(--purple)"/>
    <polygon points="223,206 270,206 280,271 205,271 205,236" fill="var(--purple)"/>
    <polygon points="581,206 628,206 646,236 646,271 571,271" fill="var(--purple)"/>
    <polygon points="205,924 280,924 270,989 213,989" fill="var(--purple)"/>
    <polygon points="571,924 646,924 638,989 581,989" fill="var(--purple)"/>
  </svg>

  <div class="tuck-logo" style="left:280px;">lumqa.</div>
  <div class="tuck-logo" style="left:646px;">lumqa.</div>

  <!-- left side -->
  <div class="side-panel left">
    <div class="side-feature" style="top:38px;">
      <svg width="30" height="28" viewBox="0 0 30 28"><circle cx="15" cy="14" r="12" fill="none" stroke="var(--pink-soft)" stroke-width="1.5"/><path d="M10 14 l4 4 l7 -8" fill="none" stroke="var(--pink-soft)" stroke-width="1.5"/></svg>
      Enamel<br>Safe</div>
    <div class="side-feature" style="top:132px;">
      <svg width="30" height="28" viewBox="0 0 30 28"><circle cx="15" cy="14" r="12" fill="none" stroke="var(--pink-soft)" stroke-width="1.5"/><path d="M10 14 l4 4 l7 -8" fill="none" stroke="var(--pink-soft)" stroke-width="1.5"/></svg>
      Maximum<br>Strength</div>
    <div class="side-feature" style="top:226px;">
      <svg width="30" height="28" viewBox="0 0 30 28"><circle cx="15" cy="14" r="12" fill="none" stroke="var(--pink-soft)" stroke-width="1.5"/><path d="M10 14 l4 4 l7 -8" fill="none" stroke="var(--pink-soft)" stroke-width="1.5"/></svg>
      Use<br>Anywhere</div>
    <div class="side-feature" style="top:320px;">
      <svg width="30" height="28" viewBox="0 0 30 28"><circle cx="15" cy="14" r="12" fill="none" stroke="var(--pink-soft)" stroke-width="1.5"/><path d="M10 14 l4 4 l7 -8" fill="none" stroke="var(--pink-soft)" stroke-width="1.5"/></svg>
      Easily<br>Brush</div>
    <div class="side-band"></div>
    <div class="side-white"></div>
    <div class="side-vertical">WHITENING<br>PEN</div>
  </div>

  <div class="front-panel">
    <div class="fp-logo">lumqa.</div>
    <div class="fp-title">WHITENING<br>PEN</div>
    <div class="fp-sub">Professional Results</div>
    <svg class="fp-nine" viewBox="0 0 66 72" aria-hidden="true">
      <circle cx="33" cy="36" r="30" fill="none" stroke="var(--pink-soft)" stroke-width="5" stroke-dasharray="1.6 3.2"/>
      <text x="27" y="58" text-anchor="middle" font-family="Outfit, sans-serif" font-weight="700" font-size="60" fill="#fff">9</text>
    </svg>
    <div class="fp-nine-text">UP TO<br>TIMES<br>WHITER</div>
    <svg class="fp-seal" viewBox="0 0 62 62" role="img" aria-label="Approval seal">
      <circle cx="31" cy="31" r="29" fill="none" stroke="#fff" stroke-width="2"/>
      <circle cx="31" cy="31" r="17" fill="none" stroke="#fff" stroke-width="1.5"/>
    </svg>
    <div class="fp-band"></div>
    <div class="fp-flavor">Mint Flavor</div>
    <div class="fp-mint" role="img" aria-label="Fresh mint leaves"></div>
    <div class="fp-white"></div>
    <ul class="fp-benefits">
      <li>Safe on Enamel</li>
      <li>Instant Effect</li>
      <li>Whiten Years of Stains</li>
    </ul>
    <div class="fp-rule"></div>
    <div class="fp-qty">4 x 2ml</div>
  </div>

  <!-- right side -->
  <div class="side-panel right">
    <div class="side-feature" style="top:38px;">
      <svg width="30" height="28" viewBox="0 0 30 28"><circle cx="15" cy="14" r="12" fill="none" stroke="#fff" stroke-width="1.5"/></svg>
      Lab<br>Approved</div>
    <div class="side-feature" style="top:132px;">
      <svg width="30" height="28" viewBox="0 0 30 28"><circle cx="15" cy="14" r="12" fill="none" stroke="var(--pink-soft)" stroke-width="1.5"/><path d="M10 14 l4 4 l7 -8" fill="none" stroke="var(--pink-soft)" stroke-width="1.5"/></svg>
      Clinicaly<br>Tested</div>
    <div class="side-feature" style="top:226px;">
      <svg width="30" height="28" viewBox="0 0 30 28"><circle cx="15" cy="14" r="12" fill="none" stroke="var(--pink-soft)" stroke-width="1.5"/><path d="M10 14 l4 4 l7 -8" fill="none" stroke="var(--pink-soft)" stroke-width="1.5"/></svg>
      Safe for<br>Sensitive teeth</div>
    <div class="side-feature" style="top:320px;">
      <svg width="30" height="28" viewBox="0 0 30 28"><circle cx="15" cy="14" r="12" fill="none" stroke="var(--pink-soft)" stroke-width="1.5"/><path d="M10 14 l4 4 l7 -8" fill="none" stroke="var(--pink-soft)" stroke-width="1.5"/></svg>
      Enamel<br>Safe</div>
    <div class="side-band"></div>
    <div class="side-white"></div>
    <div class="side-logo">lumqa.</div>
  </div>

  <!-- back -->
  <div class="back-panel">
    <div class="back-header">
      <span class="back-brand">lumqa.</span>
      <span class="back-product">WHITENING<br>PEN</span>
    </div>
    <div class="back-copy">
      <section>
        <h3>MAIN INGREDIENT</h3>
        <p>Peroxide, Glycerol, Propylene Glycol</p>
      </section>
      <section>
        <h3>CAUTION</h3>
        <ul>
          <li>Do not use the product if you are under 18 years old or pregnant, and existing dental or gum problems or have ab allergy to any of the listed ingredients.</li>
          <li>In rare cases, tooth sensitivity may occur. If sustained irritation occurs, stop using the product and seek medical advice.</li>
          <li>Use for no more than 14 consecutive day.</li>
        </ul>
      </section>
      <section>
        <h3>DIRECTIONS</h3>
        <ul>
          <li>Brush your teeth. Rotate the pen at base to dispense the gel.</li>
          <li>Hold a wide smile and keep lips away from teeth during treatment.</li>
          <li>Apply a thin layer of the gel on the tooth surface.</li>
          <li>Let the gel dry for 10 minutes then rinse mouth with warm water.</li>
          <li>Refrain from eating or drinking for 30 minutes after application.</li>
        </ul>
      </section>
      <section>
        <h3>FREQUENCY OF USE</h3>
        <ul>
          <li>Apply twice per day for up to five days. to maintain the result apply once or twice a week or as required.</li>
        </ul>
      </section>
      <section class="back-storage">
        <div>
          <h3>STORAGE</h3>
          <ul><li>Avoid sunlight and keep in cool<br>place.</li></ul>
        </div>
        <div>
          <h3>SHELF LIFE</h3>
          <p>24 Months</p>
        </div>
      </section>
    </div>
    <div class="back-rule"></div>
    <div class="back-marks" role="img" aria-label="Certification and recycling marks">
      <svg width="24" height="18"><rect x="1" y="2" width="22" height="14" rx="3" fill="#fff"/></svg>
      <svg width="18" height="18"><circle cx="9" cy="9" r="8" fill="none" stroke="#fff" stroke-width="1.5"/></svg>
      <svg width="18" height="18"><rect x="2" y="2" width="14" height="14" rx="2" fill="none" stroke="#fff" stroke-width="1.5"/></svg>
      <svg width="18" height="18"><rect x="4" y="3" width="10" height="13" rx="1" fill="#fff"/></svg>
      <svg width="18" height="18"><circle cx="9" cy="9" r="7" fill="none" stroke="#fff" stroke-width="2"/></svg>
    </div>
    <div class="back-facility">Certified Production Facility</div>
  </div>

  <div class="glue-flap"></div>
</div>

</body>
</html>
```